Small rum distillery looking for bottle design

Small rum distillery in Estonia. Looking for bottle lable design. It should be simple but at the same time point out from the variety of other bottles.
As we are a small nordic country, design can be some how nordic or represent our country. It can also have some connection with sailing or sea as we know it pirates love it.
Bottle we are using is Corvane 540

Industry/Entity Type

food and beverage

Other font styles liked:
• Baskerville

```html
<!DOCTYPE html>
<html lang="en">
<head>
<meta charset="utf-8">
<title>Halvik Distillery – Premium Estonian Rum Label</title>
<link rel="stylesheet" href="https://fonts.googleapis.com/css2?family=Libre+Baskerville:wght@400;700&family=Montserrat:wght@500;600;700&display=swap">
<style>
  :root{
    --backdrop:#d6d6d6;
    --frame:#e9e0d3;
    --sky:#dcdcdc;
    --forest:#a9a9a9;
    --ground:#2c1017;
    --diamond:#ece5db;
    --diamond-edge:#ddd2c2;
    --ink:#111111;
    --stone:#8e8e8e;
    --amber:#ec8a3a;
    --wine:#5b1a1f;
    --teal:#6aa8ac;
    --teal-light:#80b7ba;
    --navy:#1b1c30;
    --white:#ffffff;
  }
  *{margin:0;padding:0;box-sizing:border-box}
  html,body{width:1200px;height:873px;overflow:hidden;background:var(--backdrop)}
  .canvas{position:relative;width:1200px;height:873px}
  .label-frame{
    position:absolute;left:263px;top:115px;width:675px;height:647px;
    background:var(--frame);
    box-shadow:0 2px 6px rgba(0,0,0,.25);
  }
  .label{
    position:absolute;left:12px;top:9px;width:651px;height:624px;
    background:var(--sky);overflow:hidden;
  }
  .forest-scene{
    position:absolute;left:0;top:70px;width:651px;height:310px;
    background:linear-gradient(180deg,#c8c8c8 0%,var(--forest) 60%,#9f9f9f 100%);
  }
  .ground{position:absolute;left:0;top:379px;width:651px;height:245px;background:var(--ground)}
  .deer{position:absolute;background:var(--wine);border-radius:4px}
  .deer--stag{left:24px;top:256px;width:118px;height:128px}
  .deer--doe{left:555px;top:310px;width:62px;height:72px}
  .diamond{position:absolute;left:0;top:0;width:651px;height:624px}
  .brand-mark{
    position:absolute;left:309px;top:96px;width:50px;height:50px;
    border:2px solid var(--ink);border-radius:50%;
  }
  .brand-name{
    position:absolute;left:0;width:651px;top:148px;text-align:center;
    font-family:"Libre Baskerville",serif;font-weight:400;font-size:40px;
    color:var(--ink);letter-spacing:.02em;
  }
  .brand-rule{position:absolute;left:251px;top:197px;width:167px;height:2px;background:var(--ink)}
  .brand-sub{
    position:absolute;left:0;width:651px;top:202px;text-align:center;padding-left:.42em;
    font-family:"Libre Baskerville",serif;font-size:13px;letter-spacing:.42em;color:var(--ink);
  }
  .tier{
    position:absolute;left:0;width:651px;top:258px;text-align:center;padding-left:.55em;
    font-family:"Libre Baskerville",serif;font-size:20px;letter-spacing:.55em;color:var(--amber);
  }
  .origin{
    position:absolute;left:0;width:651px;top:285px;text-align:center;
    font-family:"Libre Baskerville",serif;font-weight:700;font-size:44px;color:var(--stone);
    text-shadow:1px 2px 2px rgba(0,0,0,.35);letter-spacing:-.01em;
  }
  .spirit{
    position:absolute;left:0;width:651px;top:316px;text-align:center;
    font-family:"Libre Baskerville",serif;font-weight:700;font-size:96px;color:var(--ink);
    letter-spacing:-.02em;line-height:1.2;
  }
  .spec{
    position:absolute;top:421px;font-family:"Montserrat",sans-serif;font-weight:600;
    font-size:14px;color:var(--white);
  }
  .spec em{font-family:"Libre Baskerville",serif;font-style:italic;color:var(--amber);font-weight:400}
  .spec--volume{left:41px}
  .spec--strength{left:558px}
  .age-band{
    position:absolute;left:51px;top:457px;width:570px;height:111px;
    background:var(--teal);border:2px dashed #5a9599;
  }
  .age-number{
    position:absolute;left:20px;top:6px;font-family:"Montserrat",sans-serif;font-weight:700;
    font-size:80px;color:var(--navy);line-height:1;
  }
  .age-unit{
    position:absolute;left:78px;top:84px;transform:rotate(-90deg);transform-origin:left top;
    font-family:"Montserrat",sans-serif;font-weight:500;font-size:12px;letter-spacing:.08em;color:var(--navy);
    white-space:nowrap;
  }
  .age-divider{position:absolute;left:101px;top:10px;height:88px;border-left:1px dotted rgba(27,28,48,.45)}
  .band-strip{
    position:absolute;left:107px;top:12px;width:448px;height:15px;background:var(--teal-light);
    text-align:center;font-family:"Montserrat",sans-serif;font-weight:700;font-size:11.5px;
    letter-spacing:.16em;color:var(--navy);line-height:15px;
  }
  .band-title{
    position:absolute;left:107px;width:448px;top:36px;text-align:center;padding-left:.14em;
    font-family:"Montserrat",sans-serif;font-weight:700;font-size:36px;letter-spacing:.14em;color:var(--navy);
  }
  .band-note{
    position:absolute;left:107px;width:448px;top:80px;text-align:center;
    font-family:"Montserrat",sans-serif;font-weight:500;font-size:10.5px;letter-spacing:.2em;color:var(--navy);
  }
</style>
</head>
<body>
<main class="canvas">
  <section class="label-frame">
    <div class="label">
      <div class="forest-scene" role="img" aria-label="Misty grey pine forest silhouette with a flock of dark red birds in flight"></div>
      <div class="ground"></div>
      <svg class="diamond" viewBox="0 0 651 624" aria-hidden="true">
        <polygon points="332,36 617,320 332,606 48,320" fill="var(--diamond)" stroke="var(--diamond-edge)" stroke-width="3"/>
      </svg>
      <div class="deer deer--stag" role="img" aria-label="Dark red silhouette of a stag with antlers"></div>
      <div class="deer deer--doe" role="img" aria-label="Dark red silhouette of a young deer"></div>

      <div class="brand-mark" aria-hidden="true"></div>
      <div class="brand-name">HALVIK</div>
      <div class="brand-rule"></div>
      <div class="brand-sub">DISTILLERY</div>

      <div class="tier">PREMIUM</div>
      <h1 class="origin">ESTONIAN</h1>
      <div class="spirit">RUM</div>

      <div class="spec spec--volume">500 <em>ml</em></div>
      <div class="spec spec--strength">41% <em>alc</em></div>

      <div class="age-band">
        <div class="age-number">3</div>
        <div class="age-unit">YEARS OLD</div>
        <div class="age-divider"></div>
        <div class="band-strip">PREMIUM ESTONIAN RUM</div>
        <div class="band-title">AGED IN OAK</div>
        <div class="band-note">DISTILLED FROM 100% PURE SUGARCANE</div>
      </div>
    </div>
  </section>
</main>
</body>
</html>
```